Harbinger Noble Alloys Works Business Cards

We are wanting to have a new business card designed for our company as we go to a convention. We want to balance business/Modern with elegance and beauty. Our company sells highend jewelry pieces. We want to utilize the colors of Black and Gold and have gold foiled fonts to be physically printed on the business cards.
We also would like to have space to write notes on the back side of the business card. When we meet people at jewelry conventions we would like to write notes if possible.
Here are websites and designs that we like the look and feel of these companies and you can use these as design ideas.
https://www.lorvanne.com
https://www.bellquist.com/en-us/home
Here is our company website link
www.harbingernaw.com
I also up loaded two versions of our logo.
- Update 4.26.22
I have uploaded photos of a business card we like. this card has raised embossed letters that you can feel. the raise letters are like a plastic but we don't need to use that...I uploaded to show you that we like the experience of the client feeling the characters of the logo. we also would like to have the material as a satin or some material very soft.
- Maybe we can get designs with beautiful gold foiling and raised characters and logos. we like simplicity...not busy but an elegant design. We need to write notes and would like a section where we can write notes. but we want an elegant style and the client has an experience with the feel of the card when they touch the card.
Colors
- Main colors Black & Gold
- white or light colors for small notes section.
Specialty ideals and things we would like to see based on your design styles.
- raised fonts
- raised logos
- gold foiling
- satin/soft finish on the card material.
we are wanting to design a business card that looks elegant and clean. When the client is handed the business card we want them to physically experience the business card as well by touching the raised logos or fonts and the base material is soft satin. I hope this helps with further designs.
thank you all
We uploaded a new contact layout that we have designed in our office. we would like to see how this would look on your designs.
thank you
I just finished uploading the Contact Layout. the colors are just examples. please use this layout as an idea and use colors based on the feed back we have given each of you personally.
Contact Information for Business Card
we need an area to write notes, we would like to have our logos or the diamond of our logo or the business card to have embossed sections to the business card so when the customer touches the card they can feel the logo. we would also like sections of our business card to have gold foiling. we would also like to use a satin soft paper with our card. when the client touches the card its super soft and high quality
Requirements
Must have
- we would like to have our logos or the diamond of our logo or the business card to have embossed sections to the business card so when the customer touches the card they can feel the logo. we would also like sections of our business card to have gold foiling. we would also like to use a satin soft paper with our card. when the client touches the card its super soft and high quality
Nice to have
- we would like to have our logos or the diamond of our logo or the business card to have embossed sections to the business card so when the customer touches the card they can feel the logo. we would also like sections of our business card to have gold foiling.

```html
<!DOCTYPE html>
<html lang="en">
<head>
<meta charset="utf-8">
<title>Harbinger Noble Alloys – Business Cards</title>
<link rel="stylesheet" href="https://fonts.googleapis.com/css2?family=Alegreya:wght@400;500;700&family=Alegreya+SC:wght@400;700&display=swap">
<style>
  :root {
    --backdrop: #7c8085;
    --card: #222223;
    --card-glow: #2c2c2d;
    --gold: #c99a2e;
    --gold-soft: #b8892a;
  }
  * { margin: 0; padding: 0; box-sizing: border-box; }
  html, body { width: 900px; height: 1200px; overflow: hidden; }
  body { background: var(--backdrop); position: relative; font-family: "Alegreya", serif; }

  .card {
    position: absolute;
    left: 99px;
    width: 709px;
    height: 403px;
    background: radial-gradient(ellipse at 50% 45%, var(--card-glow) 0%, var(--card) 70%);
  }
  .card--front { top: 171px; }
  .card--back { top: 680px; }

  .brand-dot {
    position: absolute;
    left: 50%;
    top: 150px;
    width: 22px;
    height: 22px;
    margin-left: -11px;
    border-radius: 50%;
    background: var(--gold);
  }
  .brand-name {
    position: absolute;
    left: 0; right: 0;
    top: 180px;
    text-align: center;
    font-family: "Alegreya SC", serif;
    font-weight: 400;
    font-size: 40px;
    line-height: 1;
    color: var(--gold);
  }
  .brand-tagline {
    position: absolute;
    left: 0; right: 0;
    top: 222px;
    text-align: center;
    font-family: "Alegreya SC", serif;
    font-size: 27px;
    line-height: 1;
    color: var(--gold-soft);
  }

  .holder { position: absolute; left: 52px; top: 40px; }
  .holder__name {
    font-family: "Alegreya SC", serif;
    font-weight: 700;
    font-size: 29px;
    letter-spacing: 0.5px;
    color: var(--gold);
    line-height: 1;
  }
  .holder__role {
    margin-top: 14px;
    font-size: 17px;
    color: var(--gold-soft);
    letter-spacing: 0.5px;
  }
  .contact { position: absolute; left: 52px; top: 190px; color: var(--gold-soft); font-size: 17.5px; letter-spacing: 0.5px; line-height: 26px; }
  .contact__phone { margin-top: 7px; }
  .contact__web { position: absolute; left: 52px; top: 314px; color: var(--gold-soft); font-size: 18px; letter-spacing: 2px; line-height: 22px; }

  .back-mark {
    position: absolute;
    left: 388px;
    width: 270px;
    top: 170px;
    text-align: center;
  }
  .back-mark__dot {
    display: block;
    width: 30px; height: 30px;
    margin: 0 auto 10px;
    border-radius: 50%;
    background: var(--gold);
  }
  .back-mark__name {
    font-family: "Alegreya SC", serif;
    font-size: 26px;
    line-height: 1;
    color: var(--gold);
  }
</style>
</head>
<body>
  <section class="card card--front">
    <span class="brand-dot"></span>
    <h1 class="brand-name">Harbinger Noble Alloys</h1>
    <p class="brand-tagline">– Coins, Jewelry &amp; Diamonds –</p>
  </section>

  <section class="card card--back">
    <div class="holder">
      <h2 class="holder__name">ELIAS MARWOOD</h2>
      <p class="holder__role">Director</p>
    </div>
    <address class="contact" style="font-style: normal;">
      2740 Larkspur Ave NE,<br>
      Dunmore, OR 97455
      <div class="contact__phone">(555) 284-7193</div>
    </address>
    <div class="contact__web">
      notes@harbingernaw.com<br>
      www.harbingernaw.com
    </div>
    <div class="back-mark">
      <span class="back-mark__dot"></span>
      <p class="back-mark__name">Harbinger Noble Alloys</p>
    </div>
  </section>
</body>
</html>
```